Classy, Elegant, Simple Business Card Design

Looking to have a classy, simple, and elegant design. Want a top notch designed business card. I really like the look of the new brivo credit card. I also like the design I attached. I am trying to reach 21-29 year old females for booking us for there wedding or event. We offer Disc Jockey Service, Photo Booth Rentals, and Uplighting .

Target Market(s)

21-28 year old females

Contact Information for Business Card

Has to have logo, website, email, and phone number

Font styles to use
Other font styles liked:
• open to font choice, modern, clean
Designer to choose
33a6d7
0791cd
0555a3
ffffff

Requirements
Must have
• Has to have logo, website, email, and phone number
Nice to have
• I really like the design of the new brivo credit card. I also included my logo and some designs I like
Should not have
• clutter or too much info

```html
<!DOCTYPE html>
<html lang="en">
<head>
<meta charset="utf-8">
<title>Tidelight Event Group – Business Card</title>
<link rel="stylesheet" href="https://fonts.googleapis.com/css2?family=Roboto:wght@300;400&display=swap">
<style>
  :root {
    --backdrop: #e9ebee;
    --card: #ffffff;
    --ink: #1c1c1c;
    --brand-mark: #c9ccd1;
    --card-edge: #dfe1e4;
  }
  * { margin: 0; padding: 0; box-sizing: border-box; }
  html, body {
    width: 1200px;
    height: 960px;
    overflow: hidden;
    background: var(--backdrop);
  }
  .stage {
    position: relative;
    width: 1200px;
    height: 960px;
  }
  .card {
    position: absolute;
    left: 75px;
    top: 180px;
    width: 1050px;
    height: 600px;
    background: var(--card);
    border: 1px solid var(--card-edge);
    border-radius: 36px;
  }
  .brand {
    position: absolute;
    right: 80px;
    top: 80px;
    text-align: center;
    color: var(--brand-mark);
    font-family: "Roboto", sans-serif;
    font-weight: 300;
    text-transform: uppercase;
  }
  .brand__name {
    display: block;
    font-size: 40px;
    letter-spacing: 4px;
    line-height: 1.1;
  }
  .brand__tagline {
    display: block;
    font-size: 16px;
    letter-spacing: 9px;
    margin-top: 6px;
  }
  .contact {
    position: absolute;
    left: 90px;
    bottom: 70px;
    list-style: none;
    font-family: "Roboto", sans-serif;
    font-weight: 400;
    font-size: 25px;
    color: var(--ink);
  }
  .contact__item {
    display: flex;
    align-items: center;
    gap: 14px;
    line-height: 38px;
  }
  .contact__icon {
    width: 18px;
    height: 18px;
    flex: none;
    fill: var(--ink);
  }
</style>
</head>
<body>
<main class="stage">
  <section class="card">
    <div class="brand">
      <span class="brand__name">Tidelight</span>
      <span class="brand__tagline">Event Group</span>
    </div>

    <ul class="contact">
      <li class="contact__item">
        <svg class="contact__icon" viewBox="0 0 24 24" aria-hidden="true">
          <path d="M6.6 10.8a15.1 15.1 0 0 0 6.6 6.6l2.2-2.2c.3-.3.7-.4 1-.2 1.1.4 2.3.6 3.6.6.6 0 1 .4 1 1V20c0 .6-.4 1-1 1A17 17 0 0 1 3 4c0-.6.4-1 1-1h3.5c.6 0 1 .4 1 1 0 1.3.2 2.5.6 3.6.1.3 0 .7-.2 1z"/>
        </svg>
        <span>555-014-2739</span>
      </li>
      <li class="contact__item">
        <svg class="contact__icon" viewBox="0 0 24 24" aria-hidden="true">
          <path d="M2 5h20v14H2z M4 7v.4l8 5.2 8-5.2V7z" fill-rule="evenodd"/>
        </svg>
        <span>info@yourmail.com</span>
      </li>
      <li class="contact__item">
        <svg class="contact__icon" viewBox="0 0 24 24" aria-hidden="true">
          <circle cx="12" cy="12" r="10"/>
        </svg>
        <span>www.yourwebsite.com</span>
      </li>
    </ul>
  </section>
</main>
</body>
</html>
```